Wine label for South African wine

modern, creative wine label name: Dravenholt The Varnex-Bund GmbH - International Wines one of the leading independent providers of inexpensive wines from around the world. The company focuses entirely on this dynamic, constantly evolving wine market, and our customers can therefore take full advantage of a complete supply chain management for themselves, including: * http://www.varnexbund.example/img/rebe.jpg procuring wines from the major producing regions around the globe * logistics and processing * wage filling and packaging * dealcoholization of wines for gastronomic purposes * design of exclusive client and proprietary brands, the target market / target group: the International market design Features; Modern, simple, meaningful, unique; Colors: gold, black, red;

Target Market(s)

Off Trade

Industry/Entity Type

Union

Font styles to use
Serif
Script

Requirements
Must have
• Modern, simple, meaningful, unique colors: gold, black, red varieties: Cab Sauv, Chard, Chenin, Merlot, Merlot Rose, Pinotage, Pinotage Rose, Shiraz, Red, Rose, White Non transparent max. Size: 12 x 9 cm data on VE: name brand, variety, country; WITHOUT Year

```html
<!DOCTYPE html>
<html lang="en">
<head>
<meta charset="UTF-8">
<title>Dravenholt – Wine Labels</title>
<link rel="stylesheet" href="https://fonts.googleapis.com/css2?family=Roboto+Slab:wght@300&family=Cormorant+Garamond:wght@500&family=Montserrat:wght@400&display=swap">
<style>
  :root {
    --page: #ffffff;
    --silver-light: #f2f2f2;
    --silver-mid: #d6d7d8;
    --silver-dark: #a9abad;
    --black-label: #1a1415;
    --black-label-edge: #0d0a0b;
    --gold-light: #c9a44a;
    --gold-mid: #a98a3a;
    --gold-dark: #6f5a24;
    --ink-dark: #1c1c1c;
    --ink-light: #e8e6e4;
    --wine-red: #b0283c;
    --wine-red-dim: #5a1420;
    --country-dim: #9a9696;
  }

  * { margin: 0; padding: 0; box-sizing: border-box; }

  html, body {
    width: 732px;
    height: 1200px;
    overflow: hidden;
    background: var(--page);
  }

  .canvas {
    position: relative;
    width: 732px;
    height: 1200px;
    display: flex;
    flex-direction: column;
    align-items: center;
    justify-content: center;
    gap: 60px;
  }

  .label {
    position: relative;
    width: 480px;
    height: 520px;
    display: flex;
    flex-direction: column;
    align-items: center;
  }

  .label--silver {
    background: linear-gradient(90deg, var(--silver-mid) 0%, var(--silver-light) 30%, var(--silver-mid) 62%, var(--silver-dark) 100%);
  }

  .label--black {
    background: linear-gradient(90deg, var(--black-label) 0%, var(--black-label) 70%, var(--black-label-edge) 100%);
  }

  .label__crest {
    margin-top: 58px;
    width: 180px;
    height: 265px;
    border-radius: 48% 48% 44% 44% / 38% 38% 62% 62%;
    background: radial-gradient(ellipse at 50% 40%, var(--gold-light) 0%, var(--gold-mid) 55%, var(--gold-dark) 100%);
  }

  .label--black .label__crest {
    background: radial-gradient(ellipse at 45% 35%, var(--gold-mid) 0%, var(--gold-dark) 70%, #3e3214 100%);
  }

  .label__brand {
    margin-top: 24px;
    font-family: "Roboto Slab", serif;
    font-weight: 300;
    font-size: 46px;
    letter-spacing: 2px;
    line-height: 1;
    color: var(--ink-dark);
  }

  .label--black .label__brand { color: var(--ink-light); }

  .label__variety {
    margin-top: 38px;
    font-family: "Cormorant Garamond", serif;
    font-weight: 500;
    font-size: 13px;
    letter-spacing: 4px;
    color: var(--wine-red);
  }

  .label--black .label__variety { color: var(--wine-red-dim); }

  .label__country {
    margin-top: 14px;
    font-family: "Montserrat", sans-serif;
    font-weight: 400;
    font-size: 15px;
    letter-spacing: 3px;
    color: var(--ink-dark);
  }

  .label--black .label__country { color: var(--country-dim); }
</style>
</head>
<body>
  <main class="canvas">
    <section class="label label--silver">
      <div class="label__crest" role="img" aria-label="Gold lion head emblem"></div>
      <h1 class="label__brand">Dravenholt</h1>
      <p class="label__variety">CABERNET SAUVIGNON</p>
      <p class="label__country">GERMANY</p>
    </section>

    <section class="label label--black">
      <div class="label__crest" role="img" aria-label="Gold lion head emblem"></div>
      <h2 class="label__brand">Dravenholt</h2>
      <p class="label__variety">CABERNET SAUVIGNON</p>
      <p class="label__country">GERMANY</p>
    </section>
  </main>
</body>
</html>
```